Smart Home App Needs 4 Mockup Screens. Extra Work Guaranteed for Winner

BACKGROUND
Our company, Marlow, is launching an exciting new app early next year. And we need some examples of what our app will look like to show to some of the biggest retailers in the world. We hope that this project will lead to regular work as we have a lot of new products planned for the app.

Our app will support baby, home and pet monitors (cameras) as well as the world's first smart pet flap.

The monitors allow you to do much more than just watch live video. By monitoring and providing information on sound, movement and temperature the app provides the user with instant peace of mind wherever they are. If anything has changed the user can be alerted via notifications. If motion is detected the user will receive a clip of the whole event moments after it has happened.

The Smart Pet Flap is packed full of features too. From letting you decide when your pet can or can't go outside from your mobile, to automatically opening if a fire is detected (along with a whole host of other features) - this really is the most advanced pet flap in the world.

REQUIREMENTS
We need 4 mock-up screens creating to show the UI of our app.
1. Camera Home Page
2. Camera Notifications Page
3. Pet Flap Fire Alarm Warning Page
4. Extreme Weather Warning Page

Optional - Happy to Pay the Winner Extra for these Designs
5. Start Up/Log In Page
6. Pet Flap Notification Example
7. Pet Flap Scheduler Page (your choice)
(SEE MARLOW APP DESIGN COMPETITION - ATTACHED)

STYLE GUIDE
As you'll see from our wireframes we want our app to be very minimal and modern. The predominant colour will be white but where colour is used it should be bright (see our colour palette - which we will provide shortly).

INSPIRATION
We love the UI of Tumbleweed (home surveillance). Also check out Pike (smart thermostat).
(SEE MARLOW UI EXAMPLES ATTACHED)

LOGO
We love our logo. Feel free to use it in creative ways.

So far we're also using it as a kind of beacon to indicate if everything is ok.

LOGO COLOURS & APP COLOURS
As mentioned, we are thinking of using the green logo to indicate that everything is ok (and also for the pet app in general). We reserve red for when something has happened (normally bad) and needs attention, like a fire alarm going off.

The app will be predominantly black and white with the odd minimal flash of colour (probably primary colour)
We'll upload a colour scheme as soon as we have it.

CONTACT
Please message us for more details - we'll do our best to reply promptly.

FUTURE WORK
We will need extra screens made straight after the competition is over and there should be additional regular work after this.

Target Market(s)

Our app will be used by young professionals, to young parents to grandparents. The design must be contemporary but timeless and easy to use no matter how good you are with technology.

Industry/Entity Type

Pet

Font styles to use
Sans Serif

Colors
faee3f
33a6d7
ec1f27
acd036
32b7a4

Requirements
Must have
• Beautiful, minimal design. Make sure you spend time looking at the Tumbleweed and Pike apps before starting.

For the videos make sure you use sensible images - that you'd expect to see from a monitor (high resolution images if possible)
Nice to have
• Creative use of our logo.
Should not have
• Too much detail/clutter/colours. Ugly fonts.

```html
<!DOCTYPE html>
<html lang="en">
<head>
<meta charset="utf-8">
<title>Marlow – Camera Home</title>
<link href="https://fonts.googleapis.com/css2?family=Open+Sans:wght@300;400;600;700&display=swap" rel="stylesheet">
<style>
  :root {
    --white: #ffffff;
    --ink: #2a2a2a;
    --muted: #9a9a9a;
    --rule: #dcdcdc;
    --alert: #ef5434;
    --ok: #8cc63f;
    --status-bg: #3c3c3c;
    --tab-bg: #2f3854;
    --tab-line: #404a68;
    --tab-icon: #c9cede;
    --active-tab: #f2f2f0;
    --timeline: #cfcfcf;
  }
  * { margin: 0; padding: 0; box-sizing: border-box; }
  html, body { width: 707px; height: 1200px; overflow: hidden; background: var(--white); }
  body { font-family: "Open Sans", Arial, sans-serif; color: var(--ink); position: relative; }

  .status-bar {
    position: absolute; left: 0; top: 0; width: 707px; height: 35px;
    background: var(--status-bg); color: #f0f0f0;
    font-family: Arial, Helvetica, sans-serif; font-weight: 700; font-size: 24px;
    display: flex; align-items: center; justify-content: space-between; padding: 0 10px;
  }
  .status-bar .carrier, .status-bar .battery { display: flex; align-items: center; gap: 6px; }
  .status-bar .time { position: absolute; left: 0; right: 0; text-align: center; pointer-events: none; }

  .app-header { position: absolute; left: 0; top: 35px; width: 707px; height: 81px; background: var(--white); border-bottom: 1px solid #ececec; }
  .menu-button { position: absolute; left: 52px; top: 28px; }
  .view-tab {
    position: absolute; top: 0; height: 81px; display: flex; align-items: center; justify-content: center;
    font-size: 12px; font-weight: 600; letter-spacing: 0.5px; color: #666;
  }
  .view-tab.now { left: 397px; width: 130px; background: var(--active-tab); }
  .view-tab.now::after {
    content: ""; position: absolute; bottom: -9px; left: 57px;
    border-left: 8px solid transparent; border-right: 8px solid transparent; border-top: 9px solid var(--active-tab);
  }
  .view-tab.earlier { left: 527px; width: 100px; }
  .brand { position: absolute; right: 10px; top: 0; height: 81px; display: flex; align-items: center; gap: 5px; font-size: 13px; font-weight: 600; color: var(--ok); }
  .brand .beacon { width: 12px; height: 12px; border-radius: 50%; background: var(--ok); }

  .live-view {
    position: absolute; left: 0; top: 116px; width: 707px; height: 351px;
    background: linear-gradient(160deg, #e9e3d8 0%, #d9cfc0 35%, #b7a594 55%, #efeae2 75%, #d8d1c6 100%);
  }

  .summary { position: absolute; left: 52px; top: 490px; font-size: 27px; font-weight: 400; color: #222; }

  .timeline-line { position: absolute; left: 78px; top: 545px; width: 2px; height: 580px; background: var(--timeline); }
  .timeline-gap { position: absolute; left: 76px; top: 822px; width: 6px; height: 100px; background: var(--white); }
  .timeline-dot { position: absolute; left: 75px; width: 8px; height: 8px; border-radius: 50%; background: var(--timeline); }

  .event { position: absolute; left: 0; width: 707px; }
  .event .snapshot {
    position: absolute; left: 25px; width: 108px; height: 108px; border-radius: 50%;
    background: linear-gradient(150deg, #f2f2f2 0%, #bdbdbd 45%, #6d6d6d 70%, #d6d6d6 100%);
  }
  .event .snapshot.patio { background: linear-gradient(160deg, #e6e6e6 0%, #6f6f6f 40%, #2f2f2f 60%, #bcbcbc 100%); }
  .event .clip-badge {
    position: absolute; left: 118px; width: 30px; height: 30px; border-radius: 50%; background: var(--alert);
    display: flex; align-items: center; justify-content: center;
  }
  .event .time { position: absolute; left: 181px; font-size: 22px; color: var(--alert); }
  .event .time small { font-size: 16px; }
  .event .detail { position: absolute; left: 181px; font-size: 21px; color: #222; white-space: nowrap; }
  .event .detail span { color: var(--muted); font-weight: 300; }
  .event .rule { position: absolute; left: 181px; width: 477px; height: 1px; background: var(--rule); }

  .tab-bar { position: absolute; left: 0; top: 1119px; width: 707px; height: 81px; background: var(--tab-bg); display: flex; }
  .tab-bar .tab { flex: 1; display: flex; align-items: center; justify-content: center; border-right: 1px solid var(--tab-line); position: relative; }
  .tab-bar .tab:last-child { border-right: none; }
  .tab-bar .count {
    position: absolute; left: 96px; top: 19px; width: 16px; height: 16px; border-radius: 50%;
    background: var(--alert); color: #fff; font-size: 10px; font-weight: 700;
    display: flex; align-items: center; justify-content: center;
  }
</style>
</head>
<body>

<div class="status-bar">
  <div class="carrier">
    <svg width="36" height="18" viewBox="0 0 36 18" fill="#f0f0f0"><rect x="0" y="12" width="4" height="6"/><rect x="7" y="9" width="4" height="9"/><rect x="14" y="6" width="4" height="12"/><rect x="21" y="3" width="4" height="15"/><rect x="28" y="0" width="4" height="18"/></svg>
    <span>DINE</span>
  </div>
  <div class="time">10:35 AM</div>
  <div class="battery">
    <svg width="20" height="20" viewBox="0 0 20 20"><circle cx="10" cy="10" r="9" fill="#f0f0f0"/><path d="M10 4v6h4" stroke="#3c3c3c" stroke-width="2" fill="none"/></svg>
    <span>65%</span>
    <svg width="40" height="20" viewBox="0 0 40 20"><rect x="1" y="2" width="33" height="16" rx="2" fill="none" stroke="#f0f0f0" stroke-width="2"/><rect x="4" y="5" width="19" height="10" fill="#f0f0f0"/><rect x="35" y="7" width="3" height="6" fill="#f0f0f0"/></svg>
  </div>
</div>

<header class="app-header">
  <svg class="menu-button" width="34" height="24" viewBox="0 0 34 24" fill="#333">
    <rect x="0" y="1" width="4" height="3"/><rect x="7" y="1" width="27" height="3"/>
    <rect x="0" y="10" width="4" height="3"/><rect x="7" y="10" width="27" height="3"/>
    <rect x="0" y="19" width="4" height="3"/><rect x="7" y="19" width="27" height="3"/>
  </svg>
  <div class="view-tab now">NOW</div>
  <div class="view-tab earlier">EARLIER</div>
  <div class="brand"><span class="beacon"></span>Marlow</div>
</header>

<div class="live-view" role="img" aria-label="Live camera view of a bright living room with cream sofas, glass coffee table, fireplace and television"></div>

<h1 class="summary">All is quiet at home</h1>

<div class="timeline-line"></div>
<div class="timeline-gap"></div>
<div class="timeline-dot" style="top:823px"></div>
<div class="timeline-dot" style="top:850px"></div>
<div class="timeline-dot" style="top:877px"></div>
<div class="timeline-dot" style="top:904px"></div>

<svg width="0" height="0" style="position:absolute">
  <defs>
    <symbol id="camera" viewBox="0 0 20 16">
      <path d="M2 3h4l2-2h4l2 2h4v12H2z" fill="#fff"/>
      <circle cx="10" cy="9" r="4" fill="none" stroke="#ef5434" stroke-width="2"/>
    </symbol>
  </defs>
</svg>

<div class="event" style="top:573px">
  <div class="snapshot" role="img" aria-label="Nursery camera snapshot"></div>
  <div class="clip-badge" style="top:4px"><svg width="17" height="14"><use href="#camera"/></svg></div>
  <div class="time" style="top:18px">7:15 <small>am</small></div>
  <div class="detail" style="top:48px">Nursery <span>- There's a lot of movement detected</span></div>
  <div class="rule" style="top:108px"></div>
</div>

<div class="event" style="top:715px">
  <div class="snapshot patio" role="img" aria-label="Patio camera snapshot"></div>
  <div class="clip-badge" style="top:4px"><svg width="17" height="14"><use href="#camera"/></svg></div>
  <div class="time" style="top:18px">5:25 <small>am</small></div>
  <div class="detail" style="top:48px">Patio <span>- Some loud noises have been heard</span></div>
  <div class="rule" style="top:108px"></div>
</div>

<div class="event" style="top:924px">
  <div class="snapshot" role="img" aria-label="Nursery camera snapshot"></div>
  <div class="clip-badge" style="top:4px"><svg width="17" height="14"><use href="#camera"/></svg></div>
  <div class="time" style="top:18px">4:57 <small>am</small></div>
  <div class="detail" style="top:48px">Nursery <span>- Slight movement has been detected</span></div>
  <div class="rule" style="top:108px"></div>
</div>

<div class="event" style="top:1065px">
  <div class="snapshot patio" role="img" aria-label="Patio camera snapshot"></div>
  <div class="clip-badge" style="top:4px"><svg width="17" height="14"><use href="#camera"/></svg></div>
  <div class="time" style="top:18px">1:02 <small>am</small></div>
</div>

<nav class="tab-bar">
  <div class="tab">
    <svg width="26" height="28" viewBox="0 0 26 28" fill="var(--tab-icon)"><circle cx="13" cy="8" r="7"/><path d="M1 28c0-8 5-12 12-12s12 4 12 12z"/></svg>
  </div>
  <div class="tab">
    <svg width="32" height="24" viewBox="0 0 32 24" fill="var(--tab-icon)"><path d="M2 5h7l3-4h8l3 4h7v18H2z"/><circle cx="16" cy="14" r="6" fill="var(--tab-bg)"/><circle cx="16" cy="14" r="3.5"/></svg>
  </div>
  <div class="tab">
    <svg width="28" height="28" viewBox="0 0 28 28" fill="var(--tab-icon)">
      <g transform="translate(14 14)">
        <rect x="-3" y="-14" width="6" height="28" rx="1"/>
        <rect x="-3" y="-14" width="6" height="28" rx="1" transform="rotate(45)"/>
        <rect x="-3" y="-14" width="6" height="28" rx="1" transform="rotate(90)"/>
        <rect x="-3" y="-14" width="6" height="28" rx="1" transform="rotate(135)"/>
        <circle r="9.5"/>
        <circle r="4" fill="var(--tab-bg)"/>
      </g>
    </svg>
  </div>
  <div class="tab">
    <svg width="28" height="28" viewBox="0 0 28 28"><circle cx="14" cy="14" r="12" fill="var(--tab-icon)"/><path d="M8 6c3 2 2 5 5 6s1 5 3 7M18 4c-1 3 3 4 5 6M5 16c3 0 4 3 4 6" stroke="var(--tab-bg)" stroke-width="2.5" fill="none"/></svg>
    <span class="count">2</span>
  </div>
</nav>

</body>
</html>
```